Halvard Cards

Technical services company
Networking, EAS, access control, project management and consultation

Clean, bold, modern design Using existing company logo for colors

Include Facebook and twitter links, QR bar code?

Industry/Entity Type

It Company

Contact Information for Business Card

Halvard Technical Services
"Steadfastly devoted to your progress"
555-318-7041 Main

Derek Lindqvo
Managing Partner / President
derek.lindqvo@halvard-ts.example
555-762-9135 Direct
www.halvard-ts.example

```html
<!DOCTYPE html>
<html lang="en">
<head>
<meta charset="utf-8">
<title>Halvard Technical Services – Business Card</title>
<link rel="stylesheet" href="https://fonts.googleapis.com/css2?family=Tinos:wght@400;700&display=swap">
<style>
  :root {
    --page: #e9e7e3;
    --paper: #ffffff;
    --paper-shade: #eef0f2;
    --blue-light: #4ab4e2;
    --blue-deep: #1f7fc4;
    --ink: #0b0b0b;
    --green: #6cc04a;
    --brand: #2a66c9;
    --tag: #4a5a8a;
    --text-dark: #111;
    --text-light: #ffffff;
  }
  * { margin: 0; padding: 0; box-sizing: border-box; }
  html, body { width: 1200px; height: 858px; overflow: hidden; }
  body {
    background: var(--page);
    font-family: "Tinos", "Times New Roman", serif;
    display: flex;
    align-items: center;
    justify-content: center;
    gap: 48px;
  }
  .card {
    position: relative;
    width: 540px;
    height: 309px;
    background: var(--paper);
    box-shadow: 0 10px 28px rgba(0,0,0,.18);
    overflow: hidden;
  }
  .card-bg { position: absolute; inset: 0; }
  .brand {
    position: absolute;
    display: flex;
    align-items: center;
    gap: 12px;
  }
  .brand-dot {
    width: 46px; height: 46px; border-radius: 50%;
    background: var(--brand);
    flex: none;
  }
  .brand-name {
    font-weight: 700;
    color: var(--brand);
    font-size: 17px;
    line-height: 1.15;
    letter-spacing: .5px;
  }
  .card-contact .brand { left: 26px; top: 122px; width: 220px; }
  .person {
    position: absolute;
    right: 28px; top: 32px;
    text-align: right;
    color: var(--text-dark);
  }
  .person-name { font-size: 27px; }
  .person-title { font-size: 13px; color: var(--text-light); margin-top: 2px; }
  .contacts {
    position: absolute;
    right: 24px; top: 140px;
    list-style: none;
    color: var(--text-light);
    font-size: 14px;
  }
  .contacts li {
    display: flex; align-items: center; justify-content: flex-end;
    gap: 10px; height: 28px;
  }
  .contacts svg { width: 14px; height: 14px; flex: none; }
  .card-front .brand {
    left: 50%; top: 104px; transform: translateX(-50%);
    flex-direction: row;
  }
  .card-front .brand-dot { width: 62px; height: 62px; }
  .card-front .brand-name { font-size: 24px; width: 200px; }
  .tagline {
    position: absolute;
    left: 0; right: 0; top: 196px;
    text-align: center;
    font-size: 14px;
    color: var(--tag);
  }
</style>
</head>
<body>

<section class="card card-contact">
  <svg class="card-bg" viewBox="0 0 540 309" preserveAspectRatio="none" aria-hidden="true">
    <defs>
      <linearGradient id="bandBlue" x1="0" y1="0" x2="1" y2="1">
        <stop offset="0" stop-color="var(--blue-deep)"/>
        <stop offset="1" stop-color="var(--blue-light)"/>
      </linearGradient>
    </defs>
    <polygon points="210,0 540,0 540,118 280,118" fill="url(#bandBlue)"/>
    <polygon points="280,118 540,118 540,309 210,309 280,150" fill="var(--ink)"/>
    <polygon points="210,0 280,118 280,150 210,309 0,309 0,0" fill="var(--paper)"/>
  </svg>

  <div class="brand">
    <span class="brand-dot"></span>
    <span class="brand-name">Halvard Technical Services</span>
  </div>

  <div class="person">
    <p class="person-name">Derek Lindqvo</p>
    <p class="person-title">Managing Partner / President</p>
  </div>

  <ul class="contacts">
    <li>555-762-9135
      <svg viewBox="0 0 14 14"><rect x="3" y="1" width="8" height="12" rx="1.5" fill="none" stroke="var(--green)" stroke-width="1.6"/></svg>
    </li>
    <li>555-318-7041
      <svg viewBox="0 0 14 14"><rect x="1" y="2" width="12" height="10" rx="2" fill="var(--green)"/><circle cx="7" cy="7" r="2.4" fill="var(--ink)"/></svg>
    </li>
    <li>www.halvard-ts.example
      <svg viewBox="0 0 14 14"><circle cx="7" cy="7" r="6" fill="var(--green)"/><path d="M1 7h12M7 1c-3 3-3 9 0 12M7 1c3 3 3 9 0 12" stroke="var(--ink)" stroke-width="1" fill="none"/></svg>
    </li>
    <li>derek.lindqvo@halvard-ts.example
      <svg viewBox="0 0 14 14"><rect x="1" y="3" width="12" height="8" fill="var(--green)"/><path d="M1 3l6 5 6-5" stroke="var(--ink)" stroke-width="1" fill="none"/></svg>
    </li>
  </ul>
</section>

<section class="card card-front">
  <div class="brand">
    <span class="brand-dot"></span>
    <span class="brand-name">Halvard Technical Services</span>
  </div>
  <p class="tagline">"Steadfastly devoted to your progress"</p>
</section>

</body>
</html>
```